Veranthex LLC, providing clean, low emission fuel for the transport and maritime industry

Veranthex LLC is a Texas based company dedicated to the development of Small Scale LNG projects with the objective of supplying clean, low emission fuel to the transport and maritime industry.

The design should be simple and sophisticated. We want a design that includes our company logo and uses our company logo colors. The site should include 7 pages (Home, About, What is LNG, Projects, Announcements and Contact Us). The site should ultimately be editable and capable of being imported into ZUMO. The design should communicate an environmentally conscious company who provide "Simple, Practical, and Cost Effective Solutions". Our competitions website looks like this www.harbvexa.com.

Target Market(s)

LNG, maritime

Industry/Entity Type

Oil And Gas

Coding

Number of Pages Required

Requirements
Must have
• Equal or better than our competitors website www.harbvexa.com
Company Logo.
The tagline "Simple, Practical, and Cost Effective Solutions"
Nice to have
• The page content will be very similar to our competitors website www.harbvexa.com
Should not have
• No red or black colours.

```html
<!DOCTYPE html>
<html lang="en">
<head>
<meta charset="utf-8">
<title>Veranthex LLC</title>
<link href="https://fonts.googleapis.com/css2?family=Poppins:wght@400;500;600;700&family=Playfair+Display:wght@400;700&display=swap" rel="stylesheet">
<style>
:root{
  --navy:#1f3b8f;
  --green:#17b03a;
  --teal:#0d6a52;
  --deep:#0e4a6b;
  --gold:#c6a200;
  --text:#2f2f2f;
  --muted:#444;
  --white:#fff;
}
*{margin:0;padding:0;box-sizing:border-box}
html,body{width:1200px;height:3327px;overflow:hidden;background:var(--white)}
body{position:relative;font-family:'Poppins',sans-serif;color:var(--text)}
.abs{position:absolute}
.btn{position:absolute;display:flex;align-items:center;justify-content:center;color:var(--white);font-size:18px;font-weight:500;text-transform:uppercase;letter-spacing:.2px}
.btn-green{background:var(--green)}
.btn-gold{background:var(--gold)}
.serif{font-family:'Playfair Display',serif;font-weight:700}

/* header */
.site-header{left:0;top:0;width:1200px;height:114px;background:var(--white);border-bottom:4px solid var(--teal);z-index:3}
.brand-tab{left:119px;top:0;width:137px;height:133px;background:var(--white);border-radius:0 0 16px 16px;z-index:4;display:flex;flex-direction:column;align-items:center;justify-content:center;gap:8px}
.brand-dot{width:46px;height:46px;border-radius:50%;background:var(--teal)}
.brand-name{font-size:15px;font-weight:700;color:var(--navy);letter-spacing:.5px}
.main-nav{left:323px;top:54px;display:flex;gap:29px;align-items:center;z-index:4}
.main-nav a{font-size:15px;font-weight:500;color:var(--text);text-decoration:none;text-transform:uppercase}
.main-nav a.active{background:var(--teal);color:var(--white);padding:7px 15px}

/* hero */
.hero{left:0;top:114px;width:1200px;height:540px;background:linear-gradient(180deg,#3b4f9e 0%,#6a5f9a 35%,#3a5a98 60%,#22437e 100%)}
.hero-title{left:119px;top:306px;font-size:45px;font-weight:700;line-height:66px;color:var(--white);letter-spacing:1px;text-transform:uppercase;z-index:2}
.hero-dots{left:556px;top:544px;display:flex;gap:12px;z-index:2}
.hero-dots span{width:14px;height:14px;border-radius:50%;background:var(--white)}
.hero-dots span.on{background:transparent;border:2px solid var(--white)}
.hero-wave{left:0;top:560px;z-index:2}

/* welcome */
.welcome-img{left:125px;top:646px;width:359px;height:478px;border-radius:180px 180px 180px 180px;background:linear-gradient(160deg,#6aa7cf 0%,#4f8fb0 40%,#4f9a6e 70%,#3f8a3a 100%)}
.welcome-title{left:545px;top:700px;font-size:34px;font-weight:700;color:var(--navy);letter-spacing:.5px;text-transform:uppercase}
.welcome-sub{left:545px;top:758px;width:500px;font-size:24px;font-weight:500;line-height:36px;color:var(--text)}
.welcome-text{left:545px;top:852px;width:536px;font-size:16.5px;line-height:25.3px;text-align:justify;color:var(--muted)}

/* stats */
.stat{width:260px;text-align:center}
.stat-num{font-family:'Playfair Display',serif;font-size:72px;font-weight:400;line-height:90px;color:#222}
.stat-label{font-size:17.5px;line-height:25px;color:var(--text);margin-top:10px}

/* split band */
.split{left:0;top:1426px}
.split-text{color:var(--white)}
.split-title{font-size:36px;letter-spacing:.5px}
.split-body{font-size:17px;line-height:25.3px;margin-top:18px;text-align:justify}

/* partners */
.section-title{left:0;width:1200px;text-align:center;font-size:36px;color:#1f1f1f;letter-spacing:.3px}
.partner{top:1957px;width:227px;height:124px;border:1px solid #d6d6d6;background:var(--white);display:flex;align-items:center;justify-content:center}
.partner i{display:block;width:150px;height:56px;border-radius:28px;background:#e6eaf0}

/* announcements */
.card-img{top:2333px;width:288px;height:231px}
.card-title{top:2592px;width:340px;text-align:center;font-size:24px;font-weight:500;color:#1f1f1f}
.card-text{top:2640px;width:300px;text-align:center;font-size:16.5px;line-height:25px;color:var(--muted)}

/* contact band */
.contact-band{left:0;top:2822px;width:1200px;height:343px}
.contact-heading{left:0;top:2905px;width:1212px;text-align:center;font-size:33px;line-height:43px;color:var(--white)}
.contact-item{display:flex;align-items:flex-start;gap:12px;color:var(--white);font-size:20px;line-height:26px}
.contact-icon{flex:none;width:46px;height:46px;border-radius:50%;background:var(--green);border:3px solid var(--white);display:flex;align-items:center;justify-content:center;margin-top:-12px}

/* footer */
.foot-brand{left:123px;top:3197px;width:110px;display:flex;flex-direction:column;align-items:center;gap:8px}
.foot-nav{left:484px;top:3217px;display:flex;gap:28px}
.foot-nav a{font-size:16.5px;color:#222;text-decoration:none}
.copyright{left:654px;top:3262px;font-size:14.5px;color:#333}
.social{top:3258px;width:30px;height:30px;border-radius:50%;background:#3f9a3a}
</style>
</head>
<body>

<header class="abs site-header"></header>
<div class="abs brand-tab"><span class="brand-dot"></span><span class="brand-name">VERANTHEX</span></div>
<nav class="abs main-nav">
  <a class="active" href="#">Home</a><a href="#">About</a><a href="#">Why LNG?</a><a href="#">Industry Partners</a><a href="#">Announcements</a><a href="#">Contact Us</a>
</nav>

<section class="abs hero" role="img" aria-label="Offshore LNG platform vessel on open sea at dusk"></section>
<h1 class="abs hero-title">Simple, Practical, and<br>Cost Effective Solutions</h1>
<div class="abs hero-dots"><span class="on"></span><span></span><span></span><span></span></div>
<svg class="abs hero-wave" width="1200" height="100" viewBox="0 0 1200 100">
  <defs><linearGradient id="waveBand" x1="0" x2="1"><stop offset="0" stop-color="#1b4f8f"/><stop offset="1" stop-color="#0d6a52"/></linearGradient></defs>
  <path d="M0 48 C300 20 700 -5 1200 10 L1200 25 C800 20 400 40 0 82Z" fill="url(#waveBand)"/>
  <path d="M0 82 C400 40 800 20 1200 25 L1200 100 L0 100Z" fill="#fff"/>
</svg>

<div class="abs welcome-img" role="img" aria-label="Refinery towers and workers in hard hats, tinted blue and green"></div>
<h2 class="abs welcome-title">Welcome to Veranthex LLC</h2>
<p class="abs welcome-sub">Bringing Low Emission Fuels to the Marine Industry</p>
<p class="abs welcome-text">Veranthex is a Texas based Company dedicated to the development of small scale LNG projects with the objective of supplying clean, low emission fuel to the transportation and maritime industry. Our Goal is to build and operate highly competitive new assets that serve the continually growing and changing needs of the North American and global LNG/natural gas market. Headquartered in Houston, Texas,</p>
<a class="btn btn-green" style="left:548px;top:1066px;width:165px;height:45px">Learn More</a>

<div class="abs stat" style="left:87px;top:1195px"><div class="stat-num">3</div><div class="stat-label">Founding Partners</div></div>
<div class="abs stat" style="left:326px;top:1195px"><div class="stat-num">85</div><div class="stat-label">Years of Industrial<br>Experience</div></div>
<div class="abs stat" style="left:590px;top:1195px"><div class="stat-num">$200B+</div><div class="stat-label">Million Dollar Profit</div></div>
<div class="abs stat" style="left:853px;top:1195px"><div class="stat-num">273</div><div class="stat-label">Satisfied Customers</div></div>

<svg class="abs split" width="1200" height="380" viewBox="0 0 1200 380">
  <defs>
    <linearGradient id="aboutFill" x1="0" x2="1"><stop offset="0" stop-color="#2d5f95"/><stop offset="1" stop-color="#133e6d"/></linearGradient>
    <linearGradient id="whyFill" x1="0" x2="1"><stop offset="0" stop-color="#2f7a3a"/><stop offset="1" stop-color="#3f8f3c"/></linearGradient>
  </defs>
  <path d="M0 0 H743 L690 380 H0Z" fill="url(#aboutFill)" role="img" aria-label="Engineers in hard hats silhouetted against a lit refinery"/>
  <path d="M756 0 H1200 V380 H698Z" fill="url(#whyFill)" role="img" aria-label="Hand holding a green globe over an industrial plant"/>
</svg>
<div class="abs split-text" style="left:119px;top:1470px;width:523px">
  <h2 class="split-title serif">ABOUT US</h2>
  <p class="split-body" style="text-align:left">Highly competitive new assets that serve the continually growing and changing needs of the North American and global LNG/natural gas market. Headquartered in Houston, Texas, Safe and reliable energy is vital to the United States &amp; the global market place. It is a force for good, providing light, heat and mobility to people around the world, and the midstream</p>
</div>
<a class="btn btn-green" style="left:121px;top:1713px;width:166px;height:45px">Learn More</a>
<div class="abs split-text" style="left:786px;top:1473px;width:346px">
  <h2 class="split-title serif">WHY LNG ?</h2>
  <p class="split-body">Our Goal is to build and operate highly competitive new assets that serve the continually growing and changing needs of the North American and global LNG/natural gas market.</p>
</div>
<a class="btn btn-gold" style="left:783px;top:1709px;width:181px;height:45px">Environmental</a>
<a class="btn btn-green" style="left:976px;top:1709px;width:156px;height:45px">Commercial</a>

<h2 class="abs section-title serif" style="top:1874px">INDUSTRIAL PARTNERS</h2>
<div class="abs partner" style="left:-119px"><i></i></div>
<div class="abs partner" style="left:125px"><i></i></div>
<div class="abs partner" style="left:368px"><i></i></div>
<div class="abs partner" style="left:605px"><i></i></div>
<div class="abs partner" style="left:846px"><i></i></div>
<div class="abs partner" style="left:1089px"><i></i></div>
<a class="btn btn-gold" style="left:517px;top:2136px;width:166px;height:45px">View All</a>

<h2 class="abs section-title serif" style="top:2243px">LATEST ANNOUNCEMENTS</h2>
<div class="abs card-img" style="left:118px;background:linear-gradient(160deg,#2a5f9a,#6b8fb4 60%,#c9b27a)" role="img" aria-label="LNG storage tanks lit at night by the harbour"></div>
<div class="abs card-img" style="left:455px;background:linear-gradient(180deg,#3c5c86,#22344e 60%,#6e6040)" role="img" aria-label="Refinery tower lit against a blue evening sky"></div>
<div class="abs card-img" style="left:792px;background:linear-gradient(120deg,#7a7a7a,#a8a8a8 50%,#d6a62c 75%,#e8e8e8)" role="img" aria-label="Engineer holding a yellow hard hat at an industrial site"></div>
<h3 class="abs card-title" style="left:91px">Low Emission Fuels</h3>
<h3 class="abs card-title" style="left:420px">Investment Strategy</h3>
<h3 class="abs card-title" style="left:760px">Expertise Resource</h3>
<p class="abs card-text" style="left:112px">LNG projects with the objective of supplying clean, .</p>
<p class="abs card-text" style="left:433px">Low emission fuel to the transportation.</p>
<p class="abs card-text" style="left:779px">Simple, Practical, and Cost Effective Solutions</p>
<a class="btn btn-green" style="left:175px;top:2715px;width:166px;height:45px">Learn More</a>
<a class="btn btn-green" style="left:509px;top:2715px;width:167px;height:45px">Learn More</a>
<a class="btn btn-green" style="left:844px;top:2715px;width:166px;height:45px">Learn More</a>

<svg class="abs contact-band" width="1200" height="343" viewBox="0 0 1200 343" role="img" aria-label="Offshore platform at night behind a green overlay">
  <defs><linearGradient id="contactFill" x1="0" y1="0" x2="0" y2="1"><stop offset="0" stop-color="#0e6a56"/><stop offset="0.6" stop-color="#1b6157"/><stop offset="1" stop-color="#2c5a78"/></linearGradient></defs>
  <path d="M0 28 C300 0 800 50 1200 5 L1200 343 L0 343Z" fill="url(#contactFill)"/>
</svg>
<h2 class="abs contact-heading serif">If you're interested in developing a LNG project for your<br>fuel needs please contact</h2>
<div class="abs contact-item" style="left:140px;top:3043px">
  <span class="contact-icon"><svg width="20" height="16" viewBox="0 0 20 16"><rect x="1" y="1" width="18" height="14" rx="2" fill="#fff"/><path d="M1 2 L10 9 L19 2" stroke="#17b03a" stroke-width="2" fill="none"/></svg></span>
  <span style="margin-top:0">Veranthex@Veranthex.com</span>
</div>
<div class="abs contact-item" style="left:483px;top:3043px">
  <span class="contact-icon"><svg width="20" height="20" viewBox="0 0 24 24"><path d="M6.6 10.8a15 15 0 006.6 6.6l2.2-2.2a1 1 0 011-.25 11.4 11.4 0 003.6.6 1 1 0 011 1V20a1 1 0 01-1 1A17 17 0 013 4a1 1 0 011-1h3.5a1 1 0 011 1c0 1.25.2 2.45.6 3.6a1 1 0 01-.25 1z" fill="#fff"/></svg></span>
  <span>(555) 014-2278</span>
</div>
<div class="abs contact-item" style="left:746px;top:3043px">
  <span class="contact-icon"><svg width="16" height="22" viewBox="0 0 16 22"><path d="M8 0C3.6 0 0 3.5 0 7.9 0 13.8 8 22 8 22s8-8.2 8-14.1C16 3.5 12.4 0 8 0z" fill="#fff"/><circle cx="8" cy="8" r="3" fill="#17b03a"/></svg></span>
  <span style="text-align:center">4870 Harbor Crest Road,<br>Port Lavon, TX 77401</span>
</div>

<footer>
  <div class="abs foot-brand"><span class="brand-dot"></span><span class="brand-name">VERANTHEX</span></div>
  <nav class="abs foot-nav"><a href="#">Home</a><a href="#">About</a><a href="#">What is LNG</a><a href="#">Projects</a><a href="#">Announcements</a><a href="#">Contact Us</a></nav>
  <p class="abs copyright">Veranthex LLC @ 2020. All Rights Reserved.</p>
  <span class="abs social" style="left:971px"></span>
  <span class="abs social" style="left:1012px"></span>
  <span class="abs social" style="left:1052px"></span>
</footer>

</body>
</html>
```